Business Card Design Project for Investment Fund

Veloria Capital Management is an emerging wealth management firm based in New Jersey. It offers superior investment returns to high net worth individuals and institutions by finding undervalued assets.
We recently selected a company logo which was inspired by the Veloria constellation. Beta Tucanae is a group of six stars, containing star cluster 47 Tucanae, rated the second brightest object in the sky.
Now we need a business card design. Since we are an investment firm, the design should project a sense of stability, growth and professionalism. The owner is interested in something simple yet striking, which of course is consistent with the logo.
Wealthy individuals, probably middle aged or older, in the US
Investment

```html
<!DOCTYPE html>
<html lang="en">
<head>
<meta charset="utf-8">
<title>Veloria Capital Management – Business Card</title>
<link rel="stylesheet" href="https://fonts.googleapis.com/css2?family=Open+Sans:wght@400;700&family=Quicksand:wght@300;400&display=swap">
<style>
  :root {
    --backdrop: #5b5b5b;
    --card-light: #f4f4f5;
    --card-mid: #dfe1e5;
    --band-dark: #111113;
    --band-edge: #2a2a2e;
    --brand-ink: #2f3a43;
    --brand-sub: #555a5e;
    --mark-blue: #2c3f9c;
    --mark-blue-deep: #1b2a78;
    --text-light: #f2f2f2;
    --text-soft: #d6d6d6;
    --ghost-ink: rgba(40, 50, 60, 0.07);
  }
  html, body {
    margin: 0;
    width: 1200px;
    height: 1000px;
    overflow: hidden;
    background: var(--backdrop);
  }
  .stage {
    width: 1200px;
    height: 1000px;
    display: flex;
    align-items: center;
    justify-content: center;
  }
  .business-card {
    width: 1089px;
    height: 594px;
    display: block;
  }
  .brand-type { font-family: "Open Sans", Arial, sans-serif; }
  .contact-type { font-family: "Quicksand", "Helvetica Neue", sans-serif; }
  .brand-name { font-weight: 700; fill: var(--brand-ink); letter-spacing: 4px; }
  .brand-sub { font-weight: 400; fill: var(--brand-sub); }
  .ghost-name { font-weight: 700; fill: var(--ghost-ink); letter-spacing: 6px; }
  .web-address { font-weight: 300; fill: #3a3a3a; letter-spacing: 0.5px; }
  .person-name { font-weight: 400; fill: var(--text-light); letter-spacing: 1px; }
  .contact-line { font-weight: 300; fill: var(--text-soft); }
  .street-address { font-weight: 400; fill: var(--text-light); letter-spacing: 0.5px; }
  .mini-name { font-weight: 700; fill: var(--text-light); letter-spacing: 1px; }
  .mini-sub { font-weight: 400; fill: var(--text-soft); }
</style>
</head>
<body>
<main class="stage">
  <svg class="business-card" viewBox="0 0 726 396" xmlns="http://www.w3.org/2000/svg" aria-label="Veloria Capital Management business card">
    <defs>
      <radialGradient id="card-surface" cx="0.5" cy="0.4" r="0.7">
        <stop offset="0" stop-color="var(--card-light)"/>
        <stop offset="1" stop-color="var(--card-mid)"/>
      </radialGradient>
      <linearGradient id="band-shade" x1="0" y1="0" x2="0" y2="1">
        <stop offset="0" stop-color="var(--band-edge)"/>
        <stop offset="0.25" stop-color="var(--band-dark)"/>
        <stop offset="1" stop-color="var(--band-dark)"/>
      </linearGradient>
      <linearGradient id="mark-fill" x1="0" y1="0" x2="0" y2="1">
        <stop offset="0" stop-color="var(--mark-blue)"/>
        <stop offset="1" stop-color="var(--mark-blue-deep)"/>
      </linearGradient>
    </defs>

    <!-- card surface -->
    <rect class="card-surface" x="0" y="0" width="726" height="396" fill="url(#card-surface)"/>

    <!-- faint brand name running behind -->
    <text class="brand-type ghost-name" x="363" y="272" font-size="82" text-anchor="middle">VELORIA</text>

    <!-- website -->
    <text class="contact-type web-address" x="714" y="17" font-size="18" text-anchor="end">www.veloriacapmgmt.com</text>

    <!-- brand block -->
    <rect class="brand-square" x="293" y="6" width="140" height="140" rx="14" fill="url(#mark-fill)"/>
    <text class="brand-type brand-name" x="363" y="196" font-size="46" text-anchor="middle">VELORIA</text>
    <text class="brand-type brand-sub" x="363" y="228" font-size="23" text-anchor="middle">Capital Management</text>

    <!-- dark wave band -->
    <path class="contact-band" d="M0,258 C140,246 270,248 360,268 C450,288 560,292 726,270 L726,396 L0,396 Z" fill="url(#band-shade)"/>

    <!-- contact details -->
    <text class="contact-type person-name" x="21" y="309" font-size="26">Daniel Hartley CEO</text>
    <text class="contact-type contact-line" x="8" y="348" font-size="18">dhartley@veloriacapmgmt.com</text>
    <text class="contact-type contact-line" x="8" y="370" font-size="17">ph: 212-555-0148</text>
    <text class="contact-type street-address" x="710" y="384" font-size="21" text-anchor="end">48 Harbor St.  Newark, NJ 07102</text>

    <!-- small brand block -->
    <rect class="mini-square" x="657" y="290" width="36" height="26" rx="3" fill="url(#mark-fill)"/>
    <text class="brand-type mini-name" x="675" y="341" font-size="12" text-anchor="middle">VELORIA</text>
    <text class="brand-type mini-sub" x="675" y="351" font-size="7" text-anchor="middle">Capital Management</text>
  </svg>
</main>
</body>
</html>
```